KelvrasMassage website required

We need a website for a mobile sports massage therapist in the United Kingdom. Specialising in pregnancy and postnatal massage, sports and remedial, deep tissue massage & Corprate Massage. Attached are some logos that we already have in various colours. The file named logo_white_background is what we normally use. Feel free to use the others at your discretion.

Requirements
Must have
• Service areas, Booking system.

```html
<!DOCTYPE html>
<html lang="en">
<head>
<meta charset="utf-8">
<title>KelvrasMassage – Services &amp; Reservation</title>
<link rel="stylesheet" href="https://fonts.googleapis.com/css2?family=Open+Sans:wght@300;400;600&family=Pirata+One&display=swap">
<style>
  :root {
    --tile-a: #3b5878;
    --tile-b: #4a6b8c;
    --tile-c: #2f4a68;
    --tile-d: #5a7fa0;
    --rule-light: #e6ebf2;
    --page-dark: #242034;
    --chevron-bg: #2a2640;
    --field-rule: #7a3558;
    --label: #a8a6b4;
    --heading: #ffffff;
    --send-text: #8d8b99;
    --divider: #5c5a6e;
  }
  * { box-sizing: border-box; margin: 0; padding: 0; }
  html, body { width: 1200px; height: 1200px; overflow: hidden; background: var(--page-dark); }
  body { position: relative; font-family: "Open Sans", Arial, sans-serif; }

  .services { position: absolute; left: 0; top: 0; width: 1200px; height: 544px; }
  .service {
    position: absolute; display: flex; align-items: center; justify-content: center;
  }
  .service--sports    { left: 0;   top: 0;   width: 598px; height: 203px; background: linear-gradient(160deg, var(--tile-a), var(--tile-c)); }
  .service--deep      { left: 598px; top: 0; width: 602px; height: 203px; background: linear-gradient(200deg, var(--tile-b), var(--tile-c)); }
  .service--pregnancy { left: 0;   top: 203px; width: 598px; height: 341px; background: linear-gradient(135deg, var(--tile-d), #4f5d92 55%, var(--tile-a)); }
  .service--corporate { left: 598px; top: 203px; width: 602px; height: 341px; background: linear-gradient(200deg, var(--tile-c), var(--tile-d) 60%, var(--tile-b)); }

  .service__title {
    position: absolute; left: 0; right: 0; text-align: center;
    font-family: "Pirata One", "Times New Roman", serif;
    font-size: 38px; color: #fff; letter-spacing: 0.5px;
  }
  .service__rule { position: absolute; width: 180px; height: 1px; background: var(--rule-light); }

  .chevron { position: absolute; left: 578px; top: 522px; width: 44px; height: 44px; }

  .reservation { position: absolute; left: 0; top: 544px; width: 1200px; height: 656px; }
  .reservation__divider { position: absolute; left: 542px; top: 111px; width: 116px; height: 1px; background: var(--divider); }
  .reservation__title {
    position: absolute; left: 0; right: 0; top: 156px; text-align: center;
    font-weight: 300; font-size: 38px; color: var(--heading); letter-spacing: 0.5px; padding-right: 6px;
  }
  .field { position: absolute; left: 338px; width: 520px; border-bottom: 1px solid var(--field-rule); text-align: center; }
  .field__label { font-size: 12.5px; color: var(--label); display: block; }
  .field--name    { top: 233px; height: 28px; }
  .field--phone   { top: 289px; height: 29px; }
  .field--email   { top: 344px; height: 34px; }
  .field--message { top: 393px; height: 123px; }
  .field__grip { position: absolute; right: 4px; bottom: 9px; width: 6px; height: 6px; }

  .send {
    position: absolute; left: 532px; top: 561px; width: 136px; height: 40px;
    border: 1px solid var(--field-rule); color: var(--send-text);
    font-size: 16px; font-weight: 600; display: flex; align-items: center; justify-content: center;
  }
</style>
</head>
<body>
  <section class="services">
    <div class="service service--sports" role="img" aria-label="Photo of a therapist stretching an athlete's leg outdoors">
      <span class="service__rule" style="top:1px"></span>
      <h2 class="service__title" style="top:19px">Sports Massage</h2>
      <span class="service__rule" style="top:85px"></span>
    </div>
    <div class="service service--deep" role="img" aria-label="Photo of a client receiving a neck and head massage">
      <span class="service__rule" style="top:1px"></span>
      <h2 class="service__title" style="top:19px">Deep Tissue Massage</h2>
      <span class="service__rule" style="top:85px"></span>
    </div>
    <div class="service service--pregnancy" role="img" aria-label="Photo of pregnant women doing side stretches on a mat">
      <span class="service__rule" style="top:162px"></span>
      <h2 class="service__title" style="top:180px">Pregnancy Massage</h2>
      <span class="service__rule" style="top:246px"></span>
    </div>
    <div class="service service--corporate" role="img" aria-label="Photo of a client relaxing during a back massage">
      <span class="service__rule" style="top:162px"></span>
      <h2 class="service__title" style="top:180px">Corprate Massage</h2>
      <span class="service__rule" style="top:246px"></span>
    </div>
    <svg class="chevron" viewBox="0 0 44 44" aria-hidden="true">
      <circle cx="22" cy="22" r="22" fill="var(--chevron-bg)"/>
      <polyline points="13,25 22,33 31,25" fill="none" stroke="#c9c7d4" stroke-width="1.3"/>
    </svg>
  </section>

  <section class="reservation">
    <span class="reservation__divider"></span>
    <h1 class="reservation__title">RESERVATION</h1>
    <div class="field field--name"><span class="field__label">Name*</span></div>
    <div class="field field--phone"><span class="field__label">Phone</span></div>
    <div class="field field--email"><span class="field__label">E-mail*</span></div>
    <div class="field field--message">
      <span class="field__label">Message*</span>
      <svg class="field__grip" viewBox="0 0 6 6" aria-hidden="true">
        <path d="M5 1V5H1M5 3V5H3" fill="none" stroke="#9a98a6" stroke-width="1"/>
      </svg>
    </div>
    <div class="send">Send</div>
  </section>
</body>
</html>
```